Android Payment Application UI Design

We require a UI/UX design for an existing Android card-based payment application.

We're looking to improve the look + feel of the existing app. What we're after:
- Colour palette options
- Fonts
- Icons

See attached document for existing screen types, icons, etc.

All resources provided must be royalty free.

It's to run on a specialised device, with 720 x 1280 pixel resolution, in portrait only (landscape not required).

Please provide mockup examples of the new screen layout applied to the existing screens in the document.

Target Market(s)

Retail business users

Font styles to use
Sans Serif

Colors

Designer to choose colors to be used in the design.

Requirements
Must have
• Looking for
• - modern design
• - simple colours, easy-to-read sans-serif fonts
• - cohesive, consistent design between screens

```html
<!DOCTYPE html>
<html lang="en">
<head>
<meta charset="utf-8">
<title>VeranPay – Screen Set</title>
<link href="https://fonts.googleapis.com/css2?family=Montserrat:wght@400;500;600;700&family=Roboto:wght@300;400&display=swap" rel="stylesheet">
<style>
  :root{
    --page:#ececec;
    --screen:#ffffff;
    --ink:#333a45;
    --brand:#1f2a5c;
    --accent:#1aa6dc;
    --button:#0ab0e6;
    --panel:#7fd3ef;
    --panel-line:#6cc4e2;
    --alert:#d82828;
    --field-line:#dcdfe4;
    --keys-bg:#e9edf3;
    --key-ink:#4f6284;
    --confirm:#5ccdc6;
    --muted:#7b8594;
  }
  *{box-sizing:border-box;margin:0;padding:0}
  html,body{width:1200px;height:1200px;overflow:hidden;background:var(--page)}
  body{position:relative;font-family:"Montserrat",sans-serif;color:var(--ink)}

  .screen{position:absolute;width:264px;height:469px;background:var(--screen);overflow:hidden}
  .col-1{left:46px}.col-2{left:470px}.col-3{left:892px}
  .row-1{top:66px}.row-2{top:678px}

  .brand{position:absolute;left:0;right:0;display:flex;align-items:center;justify-content:center;gap:6px;
         color:var(--brand);font-weight:700;letter-spacing:1px}
  .brand .dot{border-radius:50%;background:var(--accent)}
  .brand.small{top:36px;font-size:15px}
  .brand.small .dot{width:10px;height:10px}
  .brand.large{top:180px;font-size:34px;gap:12px}
  .brand.large .dot{width:26px;height:26px}
  .brand.shifted{justify-content:flex-start;padding-left:95px}

  .app-footer{position:absolute;left:0;right:0;top:441px;text-align:center;font-size:8px;font-weight:600;line-height:1}
  .app-footer small{display:block;font-size:5px;font-weight:400;color:var(--muted);margin-top:2px}

  .welcome{position:absolute;left:0;right:0;text-align:center;font-size:12.5px;color:var(--ink);letter-spacing:.3px}
  .field-label{position:absolute;left:40px;font-size:8px;font-weight:600}
  .field{position:absolute;left:40px;width:183px;height:34px;border:1px solid var(--field-line);border-radius:5px;
         font-size:9px;padding:0 5px;display:flex;align-items:center}
  .caret{display:inline-block;width:1px;height:12px;background:var(--ink);margin-left:1px}
  .login-btn{position:absolute;left:40px;top:356px;width:183px;height:34px;border-radius:4px;background:var(--button);
             color:#fff;font-size:8px;font-weight:700;letter-spacing:.6px;display:flex;align-items:center;justify-content:center}

  .keyboard{position:absolute;left:0;right:0;top:306px;bottom:0;background:var(--keys-bg);font-family:"Roboto",sans-serif;color:var(--key-ink)}
  .key-row{position:absolute;left:0;right:0;display:flex;justify-content:space-around;align-items:center;font-size:15px;font-weight:300;height:18px}
  .key{position:relative;text-align:center;width:22px;line-height:18px}
  .key sup{position:absolute;top:-8px;left:0;right:0;font-size:5px;line-height:1}
  .kb-bottom{position:absolute;top:133px;height:18px;display:flex;align-items:center}
  .space-bar{position:absolute;left:68px;top:134px;width:127px;height:16px;background:#d3dae6;border-radius:2px}
  .confirm{position:absolute;width:27px;height:27px;border-radius:50%;background:var(--confirm);display:flex;align-items:center;justify-content:center}

  .menu-dots{position:absolute;right:19px;top:51px;width:4px}
  .menu-dots i{display:block;width:3px;height:3px;border-radius:50%;background:var(--accent);margin-bottom:2px}
  .battery-pill{position:absolute;left:20px;top:79px;width:81px;height:15px;border-radius:8px;background:var(--alert);
                color:#fff;font-size:6px;font-weight:600;display:flex;align-items:center;gap:8px;padding-left:10px}
  .tabs{position:absolute;left:19px;right:18px;top:120px;display:flex;justify-content:space-between;font-size:11px}
  .tabs .active{color:var(--accent);font-weight:600}
  .menu-panel{position:absolute;left:19px;top:150px;width:226px;height:340px;background:var(--panel);border-radius:6px 6px 0 0}
  .menu-panel::before{content:"";position:absolute;left:22px;top:-8px;border:8px solid transparent;border-top:0;border-bottom-color:var(--panel)}
  .menu-item{position:absolute;left:0;right:0;height:45px;display:flex;align-items:center;font-size:11px;color:var(--ink)}
  .menu-item svg{position:absolute;left:10px;width:13px;height:13px}
  .menu-item span{position:absolute;left:34px}
  .menu-item::after{content:"";position:absolute;left:28px;right:33px;bottom:0;height:1px;background:var(--panel-line)}
  .menu-item:last-child::after{display:none}

  .dropdown{position:absolute;left:138px;top:70px;width:107px;height:172px;background:#fff;border-radius:4px;
            box-shadow:0 2px 8px rgba(0,0,0,.22);padding:4px 0}
  .dropdown-item{position:relative;height:27px;display:flex;align-items:center;font-size:6.5px;padding-left:29px}
  .dropdown-item svg{position:absolute;left:10px;width:8px;height:8px}
  .dropdown-item::after{content:"";position:absolute;left:29px;right:6px;bottom:0;height:1px;background:#e4e6ea}
  .dropdown-item:last-child::after{display:none}

  .page-title{position:absolute;left:20px;top:114px;font-size:18px;font-weight:400}
  .amount-field{font-size:17px;font-weight:700;padding-left:10px;gap:10px}
  .amount-field .currency{font-weight:400;color:#b1b6bf}
  .keypad{position:absolute;left:0;right:0;top:306px;bottom:0;background:var(--keys-bg);color:var(--key-ink);font-family:"Roboto",sans-serif}
  .pad-key{position:absolute;width:40px;text-align:center;font-size:24px;font-weight:300;line-height:1}
</style>
</head>
<body>

<!-- Splash -->
<section class="screen col-1 row-1">
  <div class="brand large"><span class="dot"></span>VERAN</div>
  <div class="app-footer">VeranPay<small>ver 0.0.1</small></div>
</section>

<!-- Login -->
<section class="screen col-2 row-1">
  <div class="brand small"><span class="dot"></span>VERAN</div>
  <p class="welcome" style="top:120px">It is nice to have you back</p>
  <label class="field-label" style="top:216px">Email address / User ID</label>
  <div class="field" style="top:230px"></div>
  <label class="field-label" style="top:289px">Password</label>
  <div class="field" style="top:303px"></div>
  <div class="login-btn">LOGIN</div>
  <div class="app-footer">VeranPay<small>ver 0.0.1</small></div>
</section>

<!-- Login with keyboard -->
<section class="screen col-3 row-1">
  <div class="brand small"><span class="dot"></span>VERAN</div>
  <p class="welcome" style="top:120px">It is nice to have you back</p>
  <label class="field-label" style="top:177px">Email address / User ID</label>
  <div class="field" style="top:192px">A<span class="caret"></span></div>
  <label class="field-label" style="top:250px">Password</label>
  <div class="field" style="top:265px"></div>
  <div class="keyboard">
    <div class="key-row" style="top:13px">
      <span class="key"><sup>1</sup>q</span><span class="key"><sup>2</sup>w</span><span class="key"><sup>3</sup>e</span><span class="key"><sup>4</sup>r</span><span class="key"><sup>5</sup>t</span><span class="key"><sup>6</sup>y</span><span class="key"><sup>7</sup>u</span><span class="key"><sup>8</sup>i</span><span class="key"><sup>9</sup>o</span><span class="key"><sup>0</sup>p</span>
    </div>
    <div class="key-row" style="top:53px;padding:0 12px">
      <span class="key">a</span><span class="key">s</span><span class="key">d</span><span class="key">f</span><span class="key">g</span><span class="key">h</span><span class="key">j</span><span class="key">k</span><span class="key">l</span>
    </div>
    <div class="key-row" style="top:93px">
      <span class="key"><svg width="14" height="16" viewBox="0 0 14 16"><path d="M7 1 L13 8 H9 V12 H5 V8 H1 Z" fill="var(--key-ink)"/><rect x="2" y="14" width="10" height="1.5" fill="var(--key-ink)"/></svg></span>
      <span class="key">z</span><span class="key">x</span><span class="key">c</span><span class="key">v</span><span class="key">b</span><span class="key">n</span><span class="key">m</span>
      <span class="key"><svg width="16" height="12" viewBox="0 0 16 12"><path d="M5 1 H15 V11 H5 L1 6 Z" fill="var(--key-ink)"/><path d="M8 4 L12 8 M12 4 L8 8" stroke="#fff" stroke-width="1.3"/></svg></span>
    </div>
    <span class="kb-bottom" style="left:8px;font-size:9px">?123</span>
    <span class="kb-bottom" style="left:52px;font-size:15px">,</span>
    <div class="space-bar"></div>
    <span class="kb-bottom" style="left:210px;font-size:15px">.</span>
    <div class="confirm" style="left:227px;top:128px"><svg width="12" height="10" viewBox="0 0 12 10"><path d="M1 5 L4.5 8.5 L11 1.5" stroke="#fff" stroke-width="1.3" fill="none"/></svg></div>
  </div>
</section>

<!-- Main menu -->
<section class="screen col-1 row-2">
  <div class="brand small shifted"><span class="dot"></span>VERAN</div>
  <div class="menu-dots"><i></i><i></i><i></i></div>
  <div class="battery-pill"><svg width="8" height="9" viewBox="0 0 8 9"><rect x="0.5" y="1" width="5" height="7.5" fill="none" stroke="#fff"/><path d="M6.5 2 L5.5 5 H7.5 L6.5 8" stroke="#fff" fill="none"/></svg>Low Battery</div>
  <nav class="tabs"><span class="active">Main menu</span><span>Admin menu</span></nav>
  <div class="menu-panel">
    <div class="menu-item" style="top:8px"><svg viewBox="0 0 14 14"><rect x="1" y="4" width="12" height="8" fill="none" stroke="currentColor"/><path d="M5 4 V2 H9 V4 M1 7 H13" stroke="currentColor" fill="none"/></svg><span>Sales</span></div>
    <div class="menu-item" style="top:53px"><svg viewBox="0 0 14 14"><path d="M4 3 L1 6 L4 9 M1 6 H10 A3 3 0 0 1 10 12 H6" stroke="currentColor" fill="none"/></svg><span>Reversal</span></div>
    <div class="menu-item" style="top:98px"><svg viewBox="0 0 14 14"><path d="M7 9 V1 M4 4 L7 1 L10 4 M1 9 V13 H13 V9" stroke="currentColor" fill="none"/></svg><span>Refund</span></div>
    <div class="menu-item" style="top:143px"><svg viewBox="0 0 14 14"><rect x="1" y="3" width="12" height="8" fill="none" stroke="currentColor"/><rect x="3" y="5" width="4" height="4" fill="none" stroke="currentColor"/><path d="M8 6 H11 M8 8 H11" stroke="currentColor"/></svg><span>Pre-Auth</span></div>
    <div class="menu-item" style="top:188px"><svg viewBox="0 0 14 14"><circle cx="7" cy="7" r="6" fill="none" stroke="currentColor"/><path d="M4 7 L6 9 L10 5" stroke="currentColor" fill="none"/></svg><span>Completion</span></div>
    <div class="menu-item" style="top:233px"><svg viewBox="0 0 14 14"><rect x="1" y="6" width="3" height="7" fill="none" stroke="currentColor"/><path d="M4 7 L7 2 Q9 2 8 6 H12 L11 13 H4" stroke="currentColor" fill="none"/></svg><span>Reconciliation</span></div>
    <div class="menu-item" style="top:278px"><svg viewBox="0 0 14 14"><rect x="1" y="5" width="12" height="6" fill="none" stroke="currentColor"/><rect x="4" y="1" width="6" height="4" fill="none" stroke="currentColor"/><rect x="4" y="9" width="6" height="4" fill="none" stroke="currentColor"/></svg><span>Reprint Manager</span></div>
  </div>
</section>

<!-- Main menu with overflow -->
<section class="screen col-2 row-2">
  <div class="brand small shifted"><span class="dot"></span>VERAN</div>
  <div class="menu-dots"><i></i><i></i><i></i></div>
  <div class="battery-pill"><svg width="8" height="9" viewBox="0 0 8 9"><rect x="0.5" y="1" width="5" height="7.5" fill="none" stroke="#fff"/><path d="M6.5 2 L5.5 5 H7.5 L6.5 8" stroke="#fff" fill="none"/></svg>Low Battery</div>
  <nav class="tabs"><span class="active">Main menu</span></nav>
  <div class="menu-panel">
    <div class="menu-item" style="top:8px"><svg viewBox="0 0 14 14"><rect x="1" y="4" width="12" height="8" fill="none" stroke="currentColor"/><path d="M5 4 V2 H9 V4 M1 7 H13" stroke="currentColor" fill="none"/></svg><span>Sales</span></div>
    <div class="menu-item" style="top:53px"><svg viewBox="0 0 14 14"><path d="M4 3 L1 6 L4 9 M1 6 H10 A3 3 0 0 1 10 12 H6" stroke="currentColor" fill="none"/></svg><span>Reversal</span></div>
    <div class="menu-item" style="top:98px"><svg viewBox="0 0 14 14"><path d="M7 9 V1 M4 4 L7 1 L10 4 M1 9 V13 H13 V9" stroke="currentColor" fill="none"/></svg><span>Refund</span></div>
    <div class="menu-item" style="top:143px"><svg viewBox="0 0 14 14"><rect x="1" y="3" width="12" height="8" fill="none" stroke="currentColor"/><rect x="3" y="5" width="4" height="4" fill="none" stroke="currentColor"/><path d="M8 6 H11 M8 8 H11" stroke="currentColor"/></svg><span>Pre-Auth</span></div>
    <div class="menu-item" style="top:188px"><svg viewBox="0 0 14 14"><circle cx="7" cy="7" r="6" fill="none" stroke="currentColor"/><path d="M4 7 L6 9 L10 5" stroke="currentColor" fill="none"/></svg><span>Completion</span></div>
    <div class="menu-item" style="top:233px"><svg viewBox="0 0 14 14"><rect x="1" y="6" width="3" height="7" fill="none" stroke="currentColor"/><path d="M4 7 L7 2 Q9 2 8 6 H12 L11 13 H4" stroke="currentColor" fill="none"/></svg><span>Reconciliation</span></div>
    <div class="menu-item" style="top:278px"><svg viewBox="0 0 14 14"><rect x="1" y="5" width="12" height="6" fill="none" stroke="currentColor"/><rect x="4" y="1" width="6" height="4" fill="none" stroke="currentColor"/><rect x="4" y="9" width="6" height="4" fill="none" stroke="currentColor"/></svg><span>Reprint Manager</span></div>
  </div>
  <div class="dropdown">
    <div class="dropdown-item"><svg viewBox="0 0 8 8"><path d="M2.5 2 A3 3 0 1 0 5.5 2 M4 0.5 V4" stroke="#999" fill="none"/></svg>Logout</div>
    <div class="dropdown-item"><svg viewBox="0 0 8 8"><circle cx="4" cy="4" r="2.6" fill="none" stroke="#999" stroke-width="1.4" stroke-dasharray="1.4 0.8"/></svg>Settings</div>
    <div class="dropdown-item"><svg viewBox="0 0 8 8"><path d="M1 3 Q4 0 7 3 M2 4.5 Q4 2.5 6 4.5" stroke="#999" fill="none"/><circle cx="4" cy="6.3" r="0.9" fill="#999"/></svg>Wifi Settings</div>
    <div class="dropdown-item"><svg viewBox="0 0 8 8"><path d="M4 1 L7 2.5 L4 4 L1 2.5 Z M1 4 L4 5.5 L7 4 M1 5.5 L4 7 L7 5.5" stroke="#999" fill="none"/></svg>Data Settings</div>
    <div class="dropdown-item"><svg viewBox="0 0 8 8"><g fill="#999"><circle cx="1.5" cy="1.5" r=".7"/><circle cx="4" cy="1.5" r=".7"/><circle cx="6.5" cy="1.5" r=".7"/><circle cx="1.5" cy="4" r=".7"/><circle cx="4" cy="4" r=".7"/><circle cx="6.5" cy="4" r=".7"/><circle cx="1.5" cy="6.5" r=".7"/><circle cx="4" cy="6.5" r=".7"/><circle cx="6.5" cy="6.5" r=".7"/></g></svg>Input Settings</div>
    <div class="dropdown-item"><svg viewBox="0 0 8 8"><path d="M1.5 1 V7 M4 1 V7 M6.5 1 V7" stroke="#999"/><path d="M0.5 3 H2.5 M3 5 H5 M5.5 2.5 H7.5" stroke="#999"/></svg>App Settings</div>
  </div>
</section>

<!-- Sales amount entry -->
<section class="screen col-3 row-2">
  <div class="brand small"><span class="dot"></span>VERAN</div>
  <div class="menu-dots"><i></i><i></i><i></i></div>
  <div class="battery-pill"><svg width="8" height="9" viewBox="0 0 8 9"><rect x="0.5" y="1" width="5" height="7.5" fill="none" stroke="#fff"/><path d="M6.5 2 L5.5 5 H7.5 L6.5 8" stroke="#fff" fill="none"/></svg>Low Battery</div>
  <h1 class="page-title">Sales</h1>
  <label class="field-label" style="top:181px">Enter Amount</label>
  <div class="field amount-field" style="top:196px"><span class="currency">£</span>500.00</div>
  <div class="keypad">
    <span class="pad-key" style="left:15px;top:8px">1</span>
    <span class="pad-key" style="left:86px;top:8px">2</span>
    <span class="pad-key" style="left:156px;top:8px">3</span>
    <span class="pad-key" style="left:218px;top:8px">-</span>
    <span class="pad-key" style="left:15px;top:48px">4</span>
    <span class="pad-key" style="left:86px;top:48px">5</span>
    <span class="pad-key" style="left:156px;top:48px">6</span>
    <span class="pad-key" style="left:218px;top:48px">,</span>
    <span class="pad-key" style="left:15px;top:90px">7</span>
    <span class="pad-key" style="left:86px;top:90px">8</span>
    <span class="pad-key" style="left:156px;top:90px">9</span>
    <span class="pad-key" style="left:218px;top:94px"><svg width="16" height="12" viewBox="0 0 16 12"><path d="M5 1 H15 V11 H5 L1 6 Z" fill="var(--key-ink)"/><path d="M8 4 L12 8 M12 4 L8 8" stroke="#fff" stroke-width="1.3"/></svg></span>
    <span class="pad-key" style="left:15px;top:130px">.</span>
    <span class="pad-key" style="left:86px;top:130px">0</span>
    <span class="pad-key" style="left:156px;top:138px;font-size:14px">00</span>
    <div class="confirm" style="left:224px;top:128px"><svg width="12" height="10" viewBox="0 0 12 10"><path d="M1 5 L4.5 8.5 L11 1.5" stroke="#fff" stroke-width="1.3" fill="none"/></svg></div>
  </div>
</section>

</body>
</html>
```